Landing page for Varkeno Computer Support

We need a high converting landing page for PPC campaign for Varkeno Computer Support. We are looking for a responsive page which works for PC, MAC and Mobile devices. Main purpose of page will be to generate calls to our Toll free number. Users can also opt for chat with technician to resolve their issues but only CTA of page should be to generate call to our toll free number.
Current landing page we use is- https://brivolhelpdesk.example/varkeno-computer-support.html (called Link1 in text below)
We will need following in new landing page:
1. Disclaimer - This is legally mandatory near CTA
GadgetMender is an independent provider of technical support services for several third party brands. If your product is under warranty or not repair service maybe available at brand owner or official website. Use of names, trademarks is for reference only. We disclaim any ownership, right, affiliation or endorsement of or by any such third party products or brands.
2. New Image of Customer Service Rep. See Link1
3. Description/details of what support for Varkeno we provide. See Link1. You can take some or all content from link1
4. Testimonials
5. Chat option
6. Footer with following- Contact Info and copyright statement. See Link1
7. You can place trust building logo like Quorbel Shield and Safenook to your choice to increase effectiveness of landing page
Take ideas from http://pagezeal.example/landing-page-articles/the-anatomy-of-a-landing-page/. We can put whatever is necessary on new landing page to reach goal of high conversions.
Landing pages designs we like:
http://www.setup-shieldware.example/5829174/quorbel/quorbel-support.html
http://www.mentorfix.example/varkeno/varkeno_support/varkeno_help_support.php
http://simplegizmo.example/fix-computer/
New Details:
-----------------
I generally prefer white background for landing pages. You can also use grey and any other color which goes with it. In the end, goal is high conversion rate.
Updates
Since some of the designs posted have ability to collect email address, I would like to clarify that Only CTA is to call toll free number. We don't need to collect email addresses. Reason is 99.9% of customers will only reach out to us if they have an urgent and immediate problem to resolve. They will call toll free and get support via remote connection but won't send email. Very few will opt to chat with technician. Even if they send email, they will never buy our services because they would have contacted somebody else to solve their immediate problem via remote connection.
Thanks
Target Market(s)
Home users and small business
Industry/Entity Type
Building
Coding
Coded - Design and coding required
Look and feel

```html
<!DOCTYPE html>
<html lang="en">
<head>
<meta charset="utf-8">
<title>Varkeno Computer Support</title>
<link rel="stylesheet" href="https://fonts.googleapis.com/css2?family=Arimo:ital,wght@0,400;0,700;1,400&family=PT+Sans:wght@400;700&family=PT+Sans+Narrow:wght@400;700&family=Raleway:wght@400&display=swap">
<style>
:root{
  --blue:#1f6cae;
  --blue-dark:#175a96;
  --blue-footer:#1b5a95;
  --ink:#222;
  --soft:#8a8a8a;
  --red:#c4122f;
  --panel-bg:#d8d8d8;
  --card-bg:#efefef;
  --frame:#dcdcdc;
  --band:#000;
  --white:#fff;
}
*{box-sizing:border-box;margin:0;padding:0}
html,body{width:1200px;height:2344px;overflow:hidden;background:var(--white)}
body{position:relative;font-family:"Arimo",Arial,sans-serif;color:var(--ink)}
.abs{position:absolute}

/* header */
.brand{display:flex;align-items:center;gap:10px;font-size:33px;color:#222;letter-spacing:-.5px}
.brand-dot{width:26px;height:26px;border-radius:50%;background:#8a8a8a}
.contact{display:flex;align-items:flex-start;gap:10px}
.contact-icon{width:26px;height:26px;border-radius:50%;background:var(--blue);display:flex;align-items:center;justify-content:center;margin-top:4px}
.contact small{display:block;font-size:15px;color:#8a8a8a;line-height:18px}
.contact span{display:block;font-size:18px;color:#111;line-height:24px}
.contact b{font-weight:700}

/* hero */
.hero-bg{left:0;top:128px;width:1200px;height:649px;background:linear-gradient(90deg,#ececec 0%,#f4f4f4 45%,#f0f0f0 70%,#f7f7f7 100%)}
.hero-strip{left:0;top:636px;width:1200px;height:141px;background:#f3f3f3}
.video{left:125px;top:216px;width:513px;height:384px;background:#c9c9c9;border:4px solid #d2d2d2}
.video-media{position:absolute;inset:0 0 44px 0;background:linear-gradient(135deg,#cfd3d6 0%,#e9e3de 40%,#b99e8e 70%,#f2f2f2 100%)}
.play{position:absolute;left:186px;top:110px;width:88px;height:88px}
.controls{position:absolute;left:0;right:0;bottom:0;height:44px;background:linear-gradient(#6a6a6a,#4a4a4a);display:flex;align-items:center;padding:0 10px;gap:10px;color:#ddd;font-size:11px}
.ctl-btn{width:22px;height:22px;border:1px solid #888;border-radius:3px;background:#555}
.track{flex:1;height:3px;background:#ddd;border-radius:2px}

.quote-avatar{left:134px;top:664px;width:78px;height:78px;border-radius:50%;border:3px solid #fff;background:radial-gradient(circle at 50% 40%,#9bb1c6,#4a6a8a);box-shadow:0 0 0 1px #ccc}
.quote-mark{font-family:Georgia,serif;font-size:54px;color:#bbb;line-height:1}
.quote-text{left:244px;top:676px;width:428px;font-size:14.2px;line-height:18px;color:#222;hyphens:auto}
.quote-name{left:244px;top:742px;font-size:14px;font-weight:700}
.quote-name em{font-style:normal;color:var(--red)}

/* call panel */
.call-panel{left:709px;top:231px;width:391px;height:583px;background:var(--panel-bg);border-radius:4px;overflow:hidden}
.panel-head{height:66px;background:linear-gradient(var(--blue),var(--blue-dark));color:#fff;font-family:"PT Sans",sans-serif;font-weight:700;font-size:29px;text-align:center;line-height:60px}
.panel-arrow{position:absolute;left:181px;top:52px;width:28px;height:28px;border-radius:50%;background:#9a9a9a;border:2px solid #e5e5e5;display:flex;align-items:center;justify-content:center}
.panel-intro{position:absolute;left:34px;top:94px;width:325px;font-family:"PT Sans",sans-serif;font-size:15px;line-height:22px;color:#333}
.tollfree{position:absolute;left:35px;top:170px;width:321px;height:52px;background:#fff;border-radius:5px;border:1px solid #ccc;display:flex;align-items:center;gap:12px;padding:0 14px}
.tollfree small{display:block;font-size:11px;color:#777;text-transform:uppercase;letter-spacing:.5px}
.tollfree b{display:block;font-size:22px;color:var(--blue-dark);line-height:24px}
.cta{position:absolute;left:35px;top:238px;width:321px;height:57px;border-radius:4px;background:linear-gradient(#2b82c6,var(--blue-dark));color:#fff;font-family:"PT Sans",sans-serif;font-size:28px;text-align:center;line-height:55px;box-shadow:0 2px 3px rgba(0,0,0,.25);text-decoration:none}
.chat{position:absolute;left:35px;top:309px;width:321px;height:36px;background:#fff;border-radius:5px;border:1px solid #ccc;display:flex;align-items:center;justify-content:center;gap:8px;font-size:14px;color:#333;text-decoration:none}
.disclaimer{position:absolute;left:35px;top:362px;width:321px;font-size:11.5px;line-height:15.5px;color:#555}
.disclaimer strong{display:block;font-size:12px;color:#333;margin-bottom:3px}

/* content */
.intro{left:122px;top:855px;width:560px;font-size:14px;line-height:21px;color:#222;letter-spacing:-.1px}
.features{left:127px;top:983px;list-style:none}
.features li{display:flex;align-items:center;gap:14px;height:50px;margin-bottom:23.5px;font-family:"PT Sans Narrow",sans-serif;font-size:21.5px;color:#222}
.num{width:50px;height:50px;border-radius:50%;background:var(--blue);color:#fff;font-family:"Arimo",sans-serif;font-size:24px;display:flex;align-items:center;justify-content:center}

.review{left:722px;top:850px;width:356px;height:345px;background:#fff;border-radius:4px;box-shadow:0 1px 5px rgba(0,0,0,.2)}
.review p{position:absolute;left:30px;top:24px;width:296px;text-align:center;font-style:italic;font-size:14px;line-height:25px;color:var(--soft)}
.review strong{position:absolute;left:0;width:100%;top:246px;text-align:center;font-size:15px;color:var(--blue-dark)}
.review-avatar{left:831px;top:1140px;width:110px;height:110px;border-radius:50%;border:3px solid var(--blue);background:radial-gradient(circle at 50% 40%,#d7bfae,#7a6a60);box-shadow:inset 0 0 0 4px #fff}

.band{left:0;top:1281px;width:1200px;height:100px;background:var(--band);color:#fff;font-family:"Raleway",sans-serif;font-size:40px;text-align:center;line-height:100px;letter-spacing:.3px}

/* cards */
.card{width:298px;height:303px;background:var(--card-bg);border-radius:3px}
.card-tab{position:absolute;left:0;top:0;width:298px;height:47px;background:linear-gradient(#2f83c8,var(--blue-dark));color:#fff;font-family:"Arimo",sans-serif;font-weight:700;font-size:23px;letter-spacing:2px;text-align:center;line-height:47px;border-radius:3px 3px 0 0}
.card-tab.grey{background:linear-gradient(#9a9a9a,#6d6d6d)}
.card-tab::after{content:"";position:absolute;left:139px;bottom:-10px;border:10px solid transparent;border-bottom:0;border-top-color:var(--blue-dark)}
.card-tab.grey::after{border-top-color:#6d6d6d}
.card-photo{position:absolute;left:22px;top:74px;width:254px;height:117px;border:7px solid var(--frame);background:linear-gradient(120deg,#dfe7ee,#b9c4cc 50%,#e9eef2)}
.card-text{position:absolute;left:28px;top:207px;width:244px;font-size:13.3px;line-height:18px;color:#222}

/* footer */
.footer{left:0;top:2159px;width:1200px;height:185px;background:var(--blue-footer);color:#fff;font-size:13px;line-height:16px}
.footer h4{font-size:13px;font-weight:700;margin-bottom:14px}
.social{display:flex;gap:9px;margin-bottom:13px}
.social i{display:block;width:27px;height:27px;border-radius:50%;background:#fff;border:3px solid #8fb3d4}
.foot-brand{display:flex;align-items:center;gap:10px;font-size:31px;color:#fff}
.foot-brand .brand-dot{background:#c9d6e3}
</style>
</head>
<body>

<!-- header -->
<div class="abs brand" style="left:98px;top:34px"><span class="brand-dot"></span>BrivolHelpdesk</div>
<div class="abs contact" style="left:638px;top:26px">
  <div class="contact-icon"><svg width="14" height="14" viewBox="0 0 14 14"><path d="M3 1l2 3-1.3 1.3a7 7 0 0 0 5 5L10 9l3 2-1 2c-6 0-11-5-11-11z" fill="#fff"/></svg></div>
  <div><small>Questions?</small><span>Call <b>00-987-654-321</b></span></div>
</div>
<div class="abs contact" style="left:895px;top:26px">
  <div class="contact-icon"><svg width="14" height="12" viewBox="0 0 14 12"><rect x="1" y="2" width="12" height="9" fill="#fff"/><path d="M1 2l6 5 6-5" fill="none" stroke="#1f6cae" stroke-width="1.4"/></svg></div>
  <div><small>Email Us:</small><span>brivolhelpdesk.example</span></div>
</div>

<!-- hero -->
<div class="abs hero-bg" role="img" aria-label="Faded background photo of a support team at work"></div>
<div class="abs hero-strip"></div>

<div class="abs video">
  <div class="video-media" role="img" aria-label="Video still of a smiling customer service representative wearing a headset"></div>
  <svg class="play" viewBox="0 0 88 88"><circle cx="44" cy="44" r="40" fill="rgba(0,0,0,.25)" stroke="#fff" stroke-width="4"/><path d="M34 26l28 18-28 18z" fill="#fff"/></svg>
  <div class="controls">
    <span class="ctl-btn"></span><span class="ctl-btn"></span>
    <span class="track"></span>
    <span>00:00/00:00</span>
    <span class="ctl-btn" style="width:36px"></span>
    <span class="ctl-btn"></span>
  </div>
</div>

<div class="abs quote-avatar" role="img" aria-label="Customer portrait"></div>
<div class="abs quote-mark" style="left:242px;top:646px">&ldquo;</div>
<div class="abs quote-mark" style="left:644px;top:722px">&rdquo;</div>
<p class="abs quote-text">Fusce porttitor elit non massa facilisis gravida. Phasellus imper&shy;diet augue quis orci commodo bibendum. Etiam nunc arcu, luctus ut ultrices quis, elementum a ligula. Aenean in congue orci</p>
<p class="abs quote-name"><em>John Doe</em>, Jordan</p>

<aside class="abs call-panel">
  <div class="panel-head">Talk to a Technician Now</div>
  <div class="panel-arrow"><svg width="12" height="8" viewBox="0 0 12 8"><path d="M1 1l5 5 5-5" fill="none" stroke="#fff" stroke-width="2"/></svg></div>
  <p class="panel-intro">Urgent computer problem? Call our certified Varkeno technicians toll free and get it fixed today by remote connection.</p>
  <div class="tollfree">
    <svg width="26" height="26" viewBox="0 0 14 14"><path d="M3 1l2 3-1.3 1.3a7 7 0 0 0 5 5L10 9l3 2-1 2c-6 0-11-5-11-11z" fill="#1f6cae"/></svg>
    <div><small>Toll-free number</small><b>00-987-654-321</b></div>
  </div>
  <a class="cta" href="tel:00987654321">Call Toll Free Now</a>
  <a class="chat" href="#chat"><svg width="18" height="16" viewBox="0 0 18 16"><path d="M2 1h14a1 1 0 0 1 1 1v9a1 1 0 0 1-1 1H7l-4 3v-3H2a1 1 0 0 1-1-1V2a1 1 0 0 1 1-1z" fill="#1f6cae"/></svg>Or chat with a technician</a>
  <p class="disclaimer"><strong>Disclaimer</strong>GadgetMender is an independent provider of technical support services for several third party brands. If your product is under warranty or not repair service maybe available at brand owner or official website. Use of names, trademarks is for reference only. We disclaim any ownership, right, affiliation or endorsement of or by any such third party products or brands.</p>
</aside>

<!-- content -->
<p class="abs intro">When you face a computer problem, identifying the problem and properly fixing it consumes precious time, labor, and resources. We are here to streamline the tech support process, offering high-quality, professional tech support for Varkeno computers. All of our technicians are fully certified and trained, with experience and expertise dealing specifically with Varkeno computers. Our technicians can efficiently deal</p>

<ol class="abs features">
  <li><span class="num">1</span>Your first feature written in the form of a benifit statement</li>
  <li><span class="num">2</span>Your Second feature written in the form of a benifit statement</li>
  <li><span class="num">3</span>Your Third feature written in the form of a benifit statement</li>
</ol>

<div class="abs review">
  <p>Aenean placerat tortor ac dui luctus ut mattis est mollis. Donec blandit orci id velit cursus varius. Fusce quam enim, hendrerit nec ultrices a, vestibulum nec enim. Quisque imperdiet ultricies dolor in convallis. Morbi sed fringilla elit. Duis sagittis lectus in orci volutpat elementum. Cras in purus sem. Curabitur augue velit, mollis in suscipit eleifend, fauci</p>
  <strong>John Doe of Kelmor Training</strong>
</div>
<div class="abs review-avatar" role="img" aria-label="Reviewer portrait"></div>

<div class="abs band">A reinforcement statement to maintain interest</div>

<!-- benefit cards -->
<div class="abs card" style="left:116px;top:1434px"><div class="card-tab">BENEFIT TITLE 1</div><div class="card-photo" role="img" aria-label="Photo of a business team"></div><p class="card-text">Vestibulum rutrum pharetra diam, eget dapibus leo vehicula ut. Fusce aliquam, odio eget adipiscing lobortis, nisl sapien placerat est...</p></div>
<div class="abs card" style="left:452px;top:1434px"><div class="card-tab">BENEFIT TITLE 2</div><div class="card-photo" role="img" aria-label="Photo of a business handshake"></div><p class="card-text">Vestibulum rutrum pharetra diam, eget dapibus leo vehicula ut. Fusce aliquam, odio eget adipiscing lobortis, nisl sapien placerat est...</p></div>
<div class="abs card" style="left:786px;top:1434px"><div class="card-tab">BENEFIT TITLE 3</div><div class="card-photo" role="img" aria-label="Photo of support agents wearing headsets"></div><p class="card-text">Vestibulum rutrum pharetra diam, eget dapibus leo vehicula ut. Fusce aliquam, odio eget adipiscing lobortis, nisl sapien placerat est...</p></div>

<div class="abs card" style="left:116px;top:1791px"><div class="card-tab grey">FEATURE 1 TITLE</div><div class="card-photo" role="img" aria-label="Photo of a business team"></div><p class="card-text">Vestibulum rutrum pharetra diam, eget dapibus leo vehicula ut. Fusce aliquam, odio eget adipiscing lobortis, nisl sapien placerat est...</p></div>
<div class="abs card" style="left:452px;top:1788px"><div class="card-tab grey">FEATURE 2 TITLE</div><div class="card-photo" role="img" aria-label="Photo of hands typing on a laptop"></div><p class="card-text">Vestibulum rutrum pharetra diam, eget dapibus leo vehicula ut. Fusce aliquam, odio eget adipiscing lobortis, nisl sapien placerat est...</p></div>
<div class="abs card" style="left:786px;top:1785px"><div class="card-tab grey">FEATURE 3 TITLE</div><div class="card-photo" role="img" aria-label="Photo of a business team"></div><p class="card-text">Vestibulum rutrum pharetra diam, eget dapibus leo vehicula ut. Fusce aliquam, odio eget adipiscing lobortis, nisl sapien placerat est...</p></div>

<!-- footer -->
<footer class="abs footer">
  <div class="abs" style="left:117px;top:38px">
    <h4>EUROPE</h4>
    <p>18 Fenwick Row<br>Dunmere, DM4 2QT</p>
    <p style="margin-top:17px">Phone:+44(0)1632 960417<br>Email:eu@norvantdata.example</p>
  </div>
  <div class="abs" style="left:323px;top:38px">
    <h4>NORTH AMERICA</h4>
    <p>4100 Larkspur Ave, Suite 210<br>Brenton, TX 75001</p>
    <p style="margin-top:17px">Phone:(555) 014 2278<br>Email:us@norvantdata.example</p>
  </div>
  <div class="abs" style="left:553px;top:38px">
    <h4>FOLLOW US ONLINE</h4>
    <div class="social"><i></i><i></i><i></i><i></i></div>
    <p>Privacy Policy | Terms of Services | Sitemap<br>Copyright © 201&nbsp; . All Rights Reserved.</p>
  </div>
  <div class="abs foot-brand" style="left:853px;top:60px"><span class="brand-dot"></span>BrivolHelpdesk</div>
</footer>

</body>
</html>
```